Quorvan Medical business cards

Double sided business cards.

Medical technology consulting company.

Business cards with two names on the front, upper to middle left:

Dr Colin R. Harbury MBBS FRACP +61412558907
Dr Owen Palatsky PhD MBusAdmin +61437619042

Email and website addresses bottom right:

colin@quorvanmedical.com.au
www.quorvanmedical.com.au

Tree logo (as per attached file) on front in a suitable position.

Tag line (as per attached files) on the back.

Need a file format to upload to Paper Haven or Cardlyner.

```html
<!DOCTYPE html>
<html lang="en">
<head>
<meta charset="utf-8">
<title>Quorvan Medical business cards</title>
<link href="https://fonts.googleapis.com/css2?family=Lato:wght@400;700&display=swap" rel="stylesheet">
<style>
  :root {
    --backdrop: #737373;
    --leaf-green: #76a22f;
    --leaf-green-light: #8dbb3c;
    --leaf-green-dark: #5f8a22;
    --cream: #fff4d6;
    --maroon: #6b0d0d;
    --white: #ffffff;
  }
  * { margin: 0; padding: 0; box-sizing: border-box; }
  html, body {
    width: 1200px; height: 1000px; overflow: hidden;
    background: var(--backdrop);
    font-family: "Lato", sans-serif;
  }
  .canvas { position: relative; width: 1200px; height: 1000px; }
  .card {
    position: absolute; left: 290px; width: 613px; height: 352px;
    border-radius: 28px; overflow: hidden;
  }
  .card--front { top: 126px; background: var(--leaf-green); }
  .card--back { top: 512px; background: var(--cream); }

  .pattern-area {
    position: absolute; inset: 0;
    background: linear-gradient(110deg, var(--leaf-green-dark) 0%, var(--leaf-green) 45%, var(--leaf-green-light) 100%);
  }

  .brand { position: absolute; display: flex; align-items: center; }
  .brand__dot { border-radius: 50%; flex: none; }
  .brand__text { display: flex; flex-direction: column; align-items: center; }
  .brand__name { font-weight: 400; letter-spacing: 0.5px; line-height: 26px; white-space: nowrap; }
  .brand__tagline { font-size: 12.5px; line-height: 15px; margin-top: 3px; white-space: nowrap; }

  .card--front .brand { left: 204px; top: 228px; gap: 44px; }
  .card--front .brand__dot { width: 42px; height: 42px; background: var(--white); }
  .card--front .brand__name { font-size: 26px; color: var(--white); }
  .card--front .brand__tagline { color: var(--white); }

  .card--back .brand { left: 306px; top: 60px; flex-direction: column; gap: 24px; }
  .card--back .brand__dot { width: 82px; height: 82px; background: var(--leaf-green); }
  .card--back .brand__name { font-size: 25px; color: var(--maroon); }
  .card--back .brand__tagline { color: var(--leaf-green); }

  .people { position: absolute; right: 360px; top: 56px; text-align: right; }
  .person + .person { margin-top: 20px; }
  .person__name { font-weight: 700; font-size: 18px; color: var(--leaf-green); line-height: 22px; }
  .person__creds, .person__phone { font-size: 17px; color: var(--maroon); line-height: 22px; }
  .person__phone { display: inline-flex; align-items: center; gap: 5px; }
  .icon { width: 11px; height: 11px; flex: none; }

  .contact { position: absolute; right: 62px; top: 279px; text-align: right; }
  .contact__line {
    display: flex; justify-content: flex-end; align-items: center; gap: 8px;
    font-size: 14.5px; color: var(--maroon); line-height: 20px;
  }
</style>
</head>
<body>
<div class="canvas">

  <section class="card card--front">
    <div class="pattern-area" role="img" aria-label="Repeating pattern of small embossed tree emblems in shades of green"></div>
    <div class="brand">
      <span class="brand__dot"></span>
      <div class="brand__text">
        <span class="brand__name">QUORVAN MEDICAL</span>
        <span class="brand__tagline">Design | Development | Launch</span>
      </div>
    </div>
  </section>

  <section class="card card--back">
    <div class="people">
      <div class="person">
        <div class="person__name">Dr. Colin R. Harbury</div>
        <div class="person__creds">MBBS FRACP</div>
        <div class="person__phone">+61412558907
          <svg class="icon" viewBox="0 0 12 12"><path d="M3 1 L5 3.5 L4 5 Q5.5 7 7 8 L8.5 7 L11 9 L9.5 11 Q4 10 1 3 Z" fill="#76a22f"/></svg>
        </div>
      </div>
      <div class="person">
        <div class="person__name">Dr. Owen Palatsky</div>
        <div class="person__creds">PhD MBusAdmin</div>
        <div class="person__phone">+61437619042
          <svg class="icon" viewBox="0 0 12 12"><path d="M3 1 L5 3.5 L4 5 Q5.5 7 7 8 L8.5 7 L11 9 L9.5 11 Q4 10 1 3 Z" fill="#76a22f"/></svg>
        </div>
      </div>
    </div>

    <div class="brand">
      <span class="brand__dot"></span>
      <div class="brand__text">
        <span class="brand__name">QUORVAN MEDICAL</span>
        <span class="brand__tagline">Design | Development | Launch</span>
      </div>
    </div>

    <div class="contact">
      <div class="contact__line">colin@quorvanmedical.com.au
        <svg class="icon" viewBox="0 0 12 12"><rect x="0.5" y="2.5" width="11" height="7.5" fill="#76a22f"/><path d="M0.5 2.5 L6 7 L11.5 2.5" fill="none" stroke="#fff4d6" stroke-width="1"/></svg>
      </div>
      <div class="contact__line">www.quorvanmedical.com.au
        <svg class="icon" viewBox="0 0 12 12"><circle cx="6" cy="6" r="5.2" fill="none" stroke="#76a22f" stroke-width="1.2"/><ellipse cx="6" cy="6" rx="2.2" ry="5.2" fill="none" stroke="#76a22f" stroke-width="1"/><path d="M1 6 H11 M2 3.5 H10 M2 8.5 H10" stroke="#76a22f" stroke-width="0.9"/></svg>
      </div>
    </div>
  </section>

</div>
</body>
</html>
```